Web application layout remake

We are looking for a makeover on our web application called “QVRcrate” - it's a document management and digital archiving system integrating workflows and allowing you to free up physical space in your office currently occupied with documents by moving them to secure external custody.
We are expecting you to include the following:
• homepage
• signup page
• application page
This project is for the whole website (which is not big at all anyway!) and not just for the design of one page. The coding should be in HTML5 only.
We are aiming for fresh, appealing, clean, user friendly ,web 2.0, jquery layout.
Remakes or changes on the logo are welcome.
The application will be sold through the portal.
Please find in attachment the print screen of the application to aid you (this is the current view customers have after logging in but the layout is obsolete and we want a brand new!).
Reason: Still not happy with the received layouts. Keep up the good work! Thanks!
Reason: Still not happy with the whole solution and finding alternate app interfaces!
Digital

```html
<!DOCTYPE html>
<html lang="en">
<head>
<meta charset="utf-8">
<title>QVRcrate — Register</title>
<link href="https://fonts.googleapis.com/css2?family=Oswald:wght@400&family=Open+Sans:wght@400;600;700&family=Pontano+Sans&family=Arimo:wght@700&display=swap" rel="stylesheet">
<style>
  :root {
    --navy: #0d3466;
    --heading: #133a6a;
    --label: #4a4a4a;
    --frame: #e4e4e4;
    --card-border: #dcdcdc;
    --body-text: #555555;
    --lead-text: #8a8a8a;
    --orange-top: #f8b52e;
    --orange-bottom: #e88f0c;
    --social: #9a9a9a;
    --white: #ffffff;
  }
  * { box-sizing: border-box; margin: 0; padding: 0; }
  html, body { width: 1200px; height: 1117px; overflow: hidden; background: var(--white); }
  body { position: relative; font-family: "Open Sans", sans-serif; color: var(--body-text); }

  .site-header { position: absolute; left: 0; top: 0; width: 1200px; height: 110px; }
  .brand {
    position: absolute; left: 21px; top: 22px; width: 220px; height: 74px;
    background: var(--navy); color: var(--white);
    font-family: "Open Sans", sans-serif; font-weight: 400; font-size: 38px;
    display: flex; align-items: center; justify-content: center; letter-spacing: 0.5px;
  }
  .main-nav a {
    position: absolute; top: 48px; font-family: "Oswald", sans-serif; font-size: 19px;
    color: var(--navy); text-decoration: none; letter-spacing: 0.5px;
  }
  .nav-new { left: 527px; }
  .nav-pricing { left: 695px; }
  .nav-trial { left: 812px; }
  .login-button {
    position: absolute; left: 1011px; top: 40px; width: 143px; height: 42px;
    border-radius: 4px; border: 1px solid #d1860c;
    background: linear-gradient(var(--orange-top), var(--orange-bottom));
    color: var(--white); font-family: "Oswald", sans-serif; font-size: 21px;
    display: flex; align-items: center; justify-content: center; letter-spacing: 0.5px;
  }

  .hero { position: absolute; left: 45px; top: 120px; width: 1110px; height: 517px; background: var(--frame); }
  .hero-panel { position: absolute; left: 18px; top: 22px; width: 1074px; height: 472px; background: var(--white); }
  .hero-title {
    position: absolute; left: 36px; top: 38px; font-family: "Oswald", sans-serif; font-weight: 400;
    font-size: 41px; line-height: 56px; color: var(--heading); letter-spacing: 1px;
  }
  .signup-form .field-label {
    position: absolute; left: 134px; font-family: "Oswald", sans-serif; font-size: 19px; line-height: 28px;
    color: var(--label); letter-spacing: 0.5px;
  }
  .signup-form .field {
    position: absolute; left: 232px; width: 307px; height: 37px;
    border: 1px solid #c6c6c6; background: linear-gradient(#ffffff, #ececec);
  }
  .label-name { top: 164px; } .field-name { top: 159px; }
  .label-company { top: 233px; } .field-company { top: 228px; }
  .label-email { top: 301px; } .field-email { top: 296px; }
  .signup-button {
    position: absolute; left: 232px; top: 378px; width: 169px; height: 47px;
    border: 1px solid #bdbdbd; border-radius: 3px; background: linear-gradient(#ffffff, #e9e9e9);
    font-family: "Open Sans", sans-serif; font-size: 13px; font-weight: 600; color: #555;
    text-align: center;
  }
  .signup-button .cap {
    position: absolute; left: 33px; top: -3px; width: 102px; height: 28px;
    border-radius: 0 0 18px 18px; border: 1px solid #2457a0;
    background: linear-gradient(#7bb7f1, #2f78cf);
  }
  .signup-button span { position: absolute; left: 0; right: 0; bottom: 4px; }
  .terms { position: absolute; left: 229px; top: 450px; font-size: 12.5px; color: #777; }
  .hero-photo {
    position: absolute; left: 752px; top: 0; width: 322px; height: 472px;
    background: radial-gradient(ellipse at 55% 55%, #c9b8a8 0%, #d9ccc0 35%, #f4f1ee 70%, #ffffff 100%);
  }
  .slider-arrow { position: absolute; top: 233px; width: 48px; height: 48px; }
  .arrow-prev { left: -30px; }
  .arrow-next { left: 1092px; }

  .plans { position: absolute; left: 0; top: 656px; }
  .plan {
    position: absolute; top: 0; width: 255px; height: 211px; border: 2px solid var(--card-border); background: var(--white);
  }
  .plan-name {
    height: 75px; border-bottom: 2px solid var(--card-border); padding-left: 16px;
    font-family: "Oswald", sans-serif; font-weight: 400; font-size: 30px; color: var(--heading);
    line-height: 75px; letter-spacing: 0.5px;
  }
  .plan-text { position: absolute; left: 16px; top: 91px; width: 140px; font-size: 14px; line-height: 23px; color: var(--body-text); }
  .plan-buy { position: absolute; left: 16px; top: 166px; font-size: 16.5px; font-weight: 600; color: #111; }
  .discount { position: absolute; left: 174px; top: 75px; width: 64px; height: 111px; }
  .gold { left: 45px; } .silver { left: 330px; } .platinum { left: 614px; } .diamond { left: 899px; }
  .silver .plan-name { padding-left: 22px; }
  .silver .plan-text, .silver .plan-buy { left: 22px; }

  .lead {
    position: absolute; left: 60px; top: 906px; width: 1080px; text-align: center;
    font-family: "Pontano Sans", sans-serif; font-size: 24.5px; line-height: 42px; color: var(--lead-text);
  }

  .site-footer { position: absolute; left: 0; top: 1026px; width: 1200px; height: 91px; border-top: 2px solid #e2e2e2; }
  .copyright { position: absolute; left: 45px; top: 37px; font-family: "Oswald", sans-serif; font-size: 14px; color: #222; letter-spacing: 0.3px; }
  .social { position: absolute; left: 886px; top: 27px; display: flex; gap: 6px; }
  .social span { width: 35px; height: 35px; border-radius: 50%; background: var(--social); display: block; }
  .social span.active { background: #111; }
</style>
</head>
<body>
  <header class="site-header">
    <div class="brand">QVRcrate</div>
    <nav class="main-nav">
      <a class="nav-new" href="#">NEW STUFF</a>
      <a class="nav-pricing" href="#">PRICING</a>
      <a class="nav-trial" href="#">60-DAY FREE TRIAL</a>
    </nav>
    <div class="login-button">USER LOGIN</div>
  </header>

  <section class="hero">
    <div class="hero-panel">
      <h1 class="hero-title">REGISTER NOW</h1>
      <div class="signup-form">
        <div class="field-label label-name">NAME</div>
        <div class="field field-name"></div>
        <div class="field-label label-company">COMANY</div>
        <div class="field field-company"></div>
        <div class="field-label label-email">E-MAIL</div>
        <div class="field field-email"></div>
        <div class="signup-button"><div class="cap"></div><span>Sign Up</span></div>
        <p class="terms">By clicking you agree to the Terms of Service, Privacy, and Refund policies.</p>
      </div>
      <div class="hero-photo" role="img" aria-label="Photo of a smiling businesswoman with arms crossed"></div>
    </div>
    <svg class="slider-arrow arrow-prev" viewBox="0 0 48 48" aria-hidden="true">
      <circle cx="24" cy="24" r="24" fill="#dcdcdc"/>
      <circle cx="24" cy="24" r="14" fill="#f4f4f4" stroke="#8a8a8a" stroke-width="2"/>
      <path d="M17 24 L28 17 L28 31 Z" fill="#777"/>
    </svg>
    <svg class="slider-arrow arrow-next" viewBox="0 0 48 48" aria-hidden="true">
      <circle cx="24" cy="24" r="24" fill="#dcdcdc"/>
      <circle cx="24" cy="24" r="14" fill="#f4f4f4" stroke="#8a8a8a" stroke-width="2"/>
      <path d="M31 24 L20 17 L20 31 Z" fill="#777"/>
    </svg>
  </section>

  <section class="plans">
    <article class="plan gold">
      <h2 class="plan-name">GOLD</h2>
      <p class="plan-text">Lorem ipsum dolor sit amet, contetuer adipiscing elit.</p>
      <div class="plan-buy">BUY NOW</div>
      <svg class="discount" viewBox="0 0 64 111"><defs><linearGradient id="rb" x1="0" y1="0" x2="0" y2="1"><stop offset="0" stop-color="#d0141b"/><stop offset="1" stop-color="#9c0d12"/></linearGradient></defs><path d="M0 0H64V111L32 96L0 111Z" fill="url(#rb)"/><text x="32" y="40" text-anchor="middle" font-family="Arimo, sans-serif" font-weight="700" font-size="25" fill="#fff">35%</text><text x="32" y="80" text-anchor="middle" font-family="Arimo, sans-serif" font-weight="700" font-size="25" fill="#fff">OFF</text></svg>
    </article>
    <article class="plan silver">
      <h2 class="plan-name">SILVER</h2>
      <p class="plan-text">Lorem ipsum dolor sit amet, contetuer adipiscing elit.</p>
      <div class="plan-buy">BUY NOW</div>
      <svg class="discount" viewBox="0 0 64 111"><path d="M0 0H64V111L32 96L0 111Z" fill="url(#rb)"/><text x="32" y="40" text-anchor="middle" font-family="Arimo, sans-serif" font-weight="700" font-size="25" fill="#fff">45%</text><text x="32" y="80" text-anchor="middle" font-family="Arimo, sans-serif" font-weight="700" font-size="25" fill="#fff">OFF</text></svg>
    </article>
    <article class="plan platinum">
      <h2 class="plan-name">PLATINIUM</h2>
      <p class="plan-text">Lorem ipsum dolor sit amet, contetuer adipiscing elit.</p>
      <div class="plan-buy">BUY NOW</div>
      <svg class="discount" viewBox="0 0 64 111"><path d="M0 0H64V111L32 96L0 111Z" fill="url(#rb)"/><text x="32" y="40" text-anchor="middle" font-family="Arimo, sans-serif" font-weight="700" font-size="25" fill="#fff">55%</text><text x="32" y="80" text-anchor="middle" font-family="Arimo, sans-serif" font-weight="700" font-size="25" fill="#fff">OFF</text></svg>
    </article>
    <article class="plan diamond">
      <h2 class="plan-name">DIAMOND</h2>
      <p class="plan-text">Lorem ipsum dolor sit amet, contetuer adipiscing elit.</p>
      <div class="plan-buy">BUY NOW</div>
      <svg class="discount" viewBox="0 0 64 111"><path d="M0 0H64V111L32 96L0 111Z" fill="url(#rb)"/><text x="32" y="40" text-anchor="middle" font-family="Arimo, sans-serif" font-weight="700" font-size="25" fill="#fff">65%</text><text x="32" y="80" text-anchor="middle" font-family="Arimo, sans-serif" font-weight="700" font-size="25" fill="#fff">OFF</text></svg>
    </article>
  </section>

  <p class="lead">Lorem ipsum dolor sit amet, consectetuer adipiscing elit. Nam cursus. Morbi ut mi. Nullam enim leo,<br>egestas id, condimenncidunt lectus quis dui viverra vestibulum.</p>

  <footer class="site-footer">
    <div class="copyright">QVRCRATE © 2013 | ALL RIGHTS RESERVED</div>
    <div class="social" aria-label="Social links">
      <span class="active"></span><span></span><span></span><span></span><span></span><span></span>
    </div>
  </footer>
</body>
</html>
```